Cascade Rhythm Guild Business Cards

The Cascade Rhythm Guild is a non-profit organization that supports, promotes, and manages music events in the Pacific Northwest. Our mission is to keep the blues alive. We do this by partnering with local venues, schools, and national acts to bring some of the best blues music to our members. As newly elected Executive Board Members we would like to have new business cards designed. I have included a copy of our logo.

```html
<!DOCTYPE html>
<html lang="en">
<head>
<meta charset="utf-8">
<title>Cascade Rhythm Guild – Business Cards</title>
<link rel="stylesheet" href="https://fonts.googleapis.com/css2?family=Arimo:wght@400;700&display=swap">
<style>
  :root {
    --stage: #2a2a2c;
    --card-dark: #353535;
    --card-light: #ffffff;
    --brand-on-dark: #f2f2f2;
    --name-blue: #4a8fdc;
    --title-red: #d3283f;
    --body-grey: #4a4a4a;
    --rule-grey: #c9c9c9;
    --icon-blue: #4a8fdc;
  }
  * { box-sizing: border-box; margin: 0; padding: 0; }
  html, body { width: 1200px; height: 874px; overflow: hidden; }
  body {
    background: var(--stage);
    font-family: "Arimo", Arial, sans-serif;
    position: relative;
  }
  .card {
    position: absolute;
    left: 250px;
    width: 700px;
    height: 400px;
    border-radius: 22px;
    box-shadow: 0 10px 28px rgba(0,0,0,.45);
  }
  .card--back { top: 24px; background: var(--card-dark); }
  .card--front { top: 450px; background: var(--card-light); }

  .brand {
    position: absolute;
    font-weight: 700;
    line-height: 1.15;
  }
  .card--back .brand {
    left: 50%; top: 50%;
    transform: translate(-50%, -50%);
    font-size: 38px;
    white-space: nowrap;
    color: var(--brand-on-dark);
  }
  .card--front .brand {
    left: 44px; top: 50%;
    transform: translateY(-50%);
    width: 290px;
    font-size: 30px;
    color: var(--name-blue);
  }

  .divider {
    position: absolute;
    left: 360px; top: 60px;
    width: 1px; height: 280px;
    background: var(--rule-grey);
  }
  .contact { position: absolute; left: 392px; top: 70px; color: var(--body-grey); }
  .contact__name { font-size: 30px; font-weight: 700; color: var(--name-blue); }
  .contact__title { font-size: 16px; color: var(--title-red); margin-top: 2px; }
  .contact__address { font-size: 17px; line-height: 1.35; margin-top: 24px; }
  .contact__list { list-style: none; margin-top: 18px; font-size: 17px; line-height: 1.45; }
  .contact__list li { display: flex; align-items: center; gap: 10px; }
  .contact__list svg { width: 14px; height: 14px; fill: var(--icon-blue); flex: none; }
</style>
</head>
<body>
  <section class="card card--back">
    <p class="brand">Cascade Rhythm Guild</p>
  </section>

  <section class="card card--front">
    <p class="brand">Cascade Rhythm Guild</p>
    <div class="divider"></div>
    <div class="contact">
      <p class="contact__name">Marcus Hale</p>
      <p class="contact__title">President</p>
      <p class="contact__address">4120 Alder Court<br>Tacoma, WA 98402</p>
      <ul class="contact__list">
        <li><svg viewBox="0 0 16 16" aria-hidden="true"><path d="M3 1l3 3-1.5 2a9 9 0 0 0 5.5 5.5L12 10l3 3-2 2C7 15 1 9 1 3z"/></svg>555-214-7730</li>
        <li><svg viewBox="0 0 16 16" aria-hidden="true"><path d="M4 0h8a1 1 0 0 1 1 1v14a1 1 0 0 1-1 1H4a1 1 0 0 1-1-1V1a1 1 0 0 1 1-1zm1 2v10h6V2zm3 11a1 1 0 1 0 0 2 1 1 0 0 0 0-2z"/></svg>555-318-6642</li>
        <li><svg viewBox="0 0 16 16" aria-hidden="true"><path d="M0 3h16v10H0zm1.5 1.2L8 9l6.5-4.8V4.2H1.5z"/></svg>hello@cascaderhythm.org</li>
        <li><svg viewBox="0 0 16 16" aria-hidden="true"><circle cx="8" cy="8" r="7"/></svg>www.cascaderhythm.org</li>
      </ul>
    </div>
  </section>
</body>
</html>
```